Namecard, letterhead & envelope
Executive Search firm
Project: Namecard, letterhead & envelope
Namecard, letterhead & envelope - Employment
Creative Brief
Professional
Derek Lim Wei Khong
President & CEO
548 Harbour Lane #05-07 Crestview Singapore 208463
dereklim@velquarepartners.example
www.velquarepartners.example
27K9053
If you think you can design a better logo, please feel free to do so. Your design should be clean, classy & professional looking. We are in the high-end headhuntng business. Background colour is white and preferably 2 colour, i.e. black plus one other colour, either gold or colour close to earth tone. But I am open to orange, yellow, brown.

```html
<!DOCTYPE html>
<html lang="en">
<head>
<meta charset="utf-8">
<title>Velquare Stationery Set</title>
<link rel="stylesheet" href="https://fonts.googleapis.com/css2?family=Arimo:wght@400;700&display=swap">
<style>
  :root {
    --brown: #5a2a14;
    --ink: #1a1a1a;
    --muted: #555555;
    --paper: #ffffff;
    --backdrop: #e9e6e2;
    --rule: #9a9a9a;
  }
  * { margin: 0; padding: 0; box-sizing: border-box; }
  html, body { width: 1200px; height: 932px; overflow: hidden; }
  body {
    background: var(--backdrop);
    font-family: "Arimo", Arial, sans-serif;
    color: var(--ink);
    position: relative;
  }
  .sheet {
    position: absolute;
    background: var(--paper);
    box-shadow: 0 2px 8px rgba(0,0,0,0.18);
  }
  .brand-name { font-weight: 700; color: var(--ink); letter-spacing: -0.5px; line-height: 1; }

  /* Fax sheet */
  .fax { left: 83px; top: 114px; width: 505px; height: 757px; z-index: 1; }
  .fax .band { position: absolute; left: 0; right: 0; top: 38px; height: 36px; background: var(--brown); }
  .fax .title { position: absolute; left: 38px; top: 190px; font-size: 34px; font-weight: 400; letter-spacing: 1px; }
  .fax .fields { position: absolute; left: 38px; top: 262px; width: 124px; }
  .fax .field { font-size: 11px; height: 32px; border-bottom: 1px solid var(--rule); padding-top: 14px; }
  .fax .checks { position: absolute; left: 38px; top: 412px; display: flex; gap: 12px; font-size: 10px; }
  .fax .check { display: flex; align-items: center; gap: 5px; }
  .fax .check i { width: 10px; height: 10px; border: 1px solid var(--muted); background: #ddd; display: block; }
  .fax .footer { position: absolute; left: 95px; top: 712px; width: 180px; font-size: 8px; line-height: 1.35; color: var(--muted); text-align: right; }

  /* Letterhead */
  .letterhead { left: 253px; top: 25px; width: 505px; height: 790px; z-index: 2; }
  .letterhead .band { position: absolute; left: 0; right: 0; top: 72px; height: 24px; background: var(--brown); }
  .letterhead .logo { position: absolute; left: 180px; top: 18px; width: 185px; padding: 6px 0 10px; background: var(--paper); text-align: center; }
  .letterhead .logo .brand-name { font-size: 44px; }
  .letterhead .footer { position: absolute; right: 22px; top: 722px; display: flex; gap: 14px; font-size: 8px; line-height: 1.45; color: var(--muted); }
  .letterhead .footer .address { text-align: right; }
  .letterhead .footer .contacts { border-left: 1px solid var(--muted); padding-left: 10px; }

  /* Envelope */
  .envelope { left: 493px; top: 328px; width: 568px; height: 278px; z-index: 3; overflow: hidden; }
  .envelope .flap { position: absolute; left: 0; right: 0; top: 0; height: 46px; background: var(--brown); }
  .envelope .flap-name { position: absolute; right: 160px; top: 12px; font-size: 20px; font-weight: 700; color: var(--paper); transform: rotate(180deg); }
  .envelope .logo { position: absolute; left: 30px; top: 58px; }
  .envelope .logo .brand-name { font-size: 40px; }
  .envelope .address { position: absolute; left: 52px; top: 236px; font-size: 8px; line-height: 1.4; color: var(--muted); }

  /* Business card */
  .card { left: 854px; top: 88px; width: 270px; height: 152px; z-index: 3; }
  .card .band { position: absolute; left: 0; right: 0; top: 16px; height: 24px; background: var(--brown); }
  .card .logo { position: absolute; left: 80px; top: 8px; width: 112px; padding: 4px 0 6px; background: var(--paper); text-align: center; }
  .card .logo .brand-name { font-size: 26px; }
  .card .person { position: absolute; left: 0; right: 0; top: 52px; text-align: center; font-size: 7.5px; line-height: 1.3; }
  .card .person .name { font-weight: 700; }
  .card .details { position: absolute; left: 78px; top: 76px; display: flex; gap: 10px; font-size: 6.5px; line-height: 1.45; color: var(--muted); }
  .card .details .contacts { border-left: 1px solid var(--muted); padding-left: 7px; }
</style>
</head>
<body>

  <section class="sheet fax" aria-label="Fax cover sheet">
    <div class="band"></div>
    <h2 class="title">FAX</h2>
    <div class="fields">
      <div class="field">To:</div>
      <div class="field">Fax:</div>
      <div class="field">Phone:</div>
      <div class="field">Re:</div>
    </div>
    <div class="checks">
      <span class="check"><i></i>Urgent</span>
      <span class="check"><i></i>For Review</span>
    </div>
    <div class="footer">
      548 Harbour Lane<br>#05-07 Crestview Singapore 208463<br>Licence No: 27K9053
    </div>
  </section>

  <section class="sheet letterhead" aria-label="Letterhead">
    <div class="band"></div>
    <div class="logo">
      <div class="brand-name">Velquare</div>
    </div>
    <div class="footer">
      <div class="address">548 Harbour Lane<br>#05-07 Crestview Singapore 208463<br>Licence No: 27K9053</div>
      <div class="contacts">T +65 6200 1480 &nbsp; M +65 9311 2750 &nbsp; F +65 6200 1481<br>E dereklim@velquarepartners.example<br>W www.velquarepartners.example</div>
    </div>
  </section>

  <section class="sheet envelope" aria-label="Envelope">
    <div class="flap"><span class="flap-name">Velquare</span></div>
    <div class="logo">
      <div class="brand-name">Velquare</div>
    </div>
    <div class="address">548 Harbour Lane #05-07 Crestview Singapore 208463<br>www.velquarepartners.example</div>
  </section>

  <section class="sheet card" aria-label="Business card">
    <div class="band"></div>
    <div class="logo">
      <div class="brand-name">Velquare</div>
    </div>
    <div class="person">
      <div class="name">Derek Lim Wei Khong</div>
      <div>President &amp; CEO</div>
    </div>
    <div class="details">
      <div class="address">548 Harbour Lane<br>#05-07 Crestview<br>Singapore 208463</div>
      <div class="contacts">T +65 6200 1480<br>M +65 9311 2750<br>dereklim@velquarepartners.example<br>www.velquarepartners.example</div>
    </div>
  </section>

</body>
</html>
```